I need a business card.

I need a simple, minimalist, business card. I think the coolest business card I have ever seen is Marty Vexler's from Kestrel's 9... it is just a little creepy for the real world.
I am a photographer and I need a card that I can give to brides or potential portrait customers that is simple and classy.
My name is Glen Hardesty. My website is www.glenhardesty-example.com
Please design my card.
I think it could be as simple as my name, phone # and website... where the rest of my contact could be found... or maybe my email and no website... I am open to ideas. I imagined the card on thick card stock with a black background...

```html
<!DOCTYPE html>
<html lang="en">
<head>
<meta charset="utf-8">
<title>Glen Hardesty — Photographer Business Card</title>
<link rel="stylesheet" href="https://fonts.googleapis.com/css2?family=Quicksand:wght@400;500;600&family=Exo+2:wght@500&display=swap">
<style>
  :root {
    --backdrop: #d9d4cc;
    --card-black: #000000;
    --ink-white: #ffffff;
    --ink-light: #e6e6e6;
    --ink-grey: #7a7a7a;
    --band-grey: #6b6b6b;
    --icon-grey: #8c8c8c;
  }
  * { margin: 0; padding: 0; box-sizing: border-box; }
  html, body {
    width: 1200px;
    height: 900px;
    overflow: hidden;
    background: var(--backdrop);
    font-family: "Quicksand", sans-serif;
  }
  .canvas {
    position: relative;
    width: 1200px;
    height: 900px;
  }
  .card {
    position: absolute;
    width: 600px;
    height: 349px;
    background: var(--card-black);
    box-shadow: 0 3px 10px rgba(0,0,0,0.25);
  }
  /* Front */
  .card-front { left: 105px; top: 92px; }
  .brand {
    position: absolute;
    left: 0;
    right: 0;
    top: 166px;
    text-align: center;
  }
  .brand-name {
    font-family: "Quicksand", sans-serif;
    font-weight: 500;
    font-size: 50px;
    line-height: 1;
    color: var(--ink-white);
    letter-spacing: 0.5px;
  }
  .brand-role {
    margin-top: 2px;
    font-weight: 500;
    font-size: 20px;
    color: var(--ink-grey);
    letter-spacing: 0.3px;
  }
  /* Back */
  .card-back { left: 480px; top: 471px; }
  .edge-band {
    position: absolute;
    left: 0; top: 0;
    width: 14px; height: 100%;
    background: var(--band-grey);
  }
  .contact-row {
    position: absolute;
    left: 68px;
    display: flex;
    align-items: center;
    gap: 14px;
    color: var(--ink-light);
  }
  .contact-row svg { flex: none; }
  .phone { top: 67px; }
  .phone .contact-text {
    font-family: "Exo 2", sans-serif;
    font-weight: 500;
    font-size: 22px;
    color: var(--ink-white);
  }
  .email { top: 107px; }
  .email .contact-text { font-size: 20px; font-weight: 500; }
  .social-list {
    position: absolute;
    left: 74px;
    top: 190px;
    list-style: none;
  }
  .social-list li {
    display: flex;
    align-items: center;
    gap: 12px;
    height: 32.5px;
    font-size: 21px;
    font-weight: 500;
    color: var(--ink-light);
  }
  .social-mark {
    width: 22px; height: 22px;
    border: 1.5px solid var(--icon-grey);
    border-radius: 3px;
    flex: none;
  }
  .web-band {
    position: absolute;
    right: 0;
    bottom: 0;
    height: 45px;
    padding: 0 10px 0 12px;
    background: var(--band-grey);
    color: var(--ink-white);
    font-size: 17px;
    font-weight: 500;
    line-height: 45px;
  }
</style>
</head>
<body>
<main class="canvas">
  <section class="card card-front" aria-label="Card front">
    <div class="brand">
      <h1 class="brand-name">Glen Hardesty</h1>
      <p class="brand-role">photographer</p>
    </div>
  </section>

  <section class="card card-back" aria-label="Card back">
    <div class="edge-band"></div>

    <div class="contact-row phone">
      <svg width="24" height="24" viewBox="0 0 24 24" aria-hidden="true">
        <circle cx="12" cy="12" r="10.5" fill="none" stroke="var(--icon-grey)" stroke-width="1.5"/>
        <path d="M8.5 6.5c.6-.4 1.3-.2 1.6.4l1 1.8c.3.5.1 1.1-.3 1.4l-.7.5c.5 1.4 1.6 2.6 3 3.2l.5-.7c.3-.4.9-.6 1.4-.3l1.8 1c.6.3.8 1 .4 1.6l-.6.9c-.5.7-1.4 1-2.2.7-3.2-1.1-5.6-3.6-6.6-6.8-.3-.8 0-1.6.7-2.1z" fill="var(--icon-grey)"/>
      </svg>
      <span class="contact-text">555.014.2290</span>
    </div>

    <div class="contact-row email">
      <svg width="28" height="20" viewBox="0 0 28 20" aria-hidden="true">
        <g fill="none" stroke="var(--icon-grey)" stroke-width="1.3">
          <path d="M2 6 L22 1 L26 14 L6 19 Z"/>
          <path d="M2 6 L15 11 L22 1"/>
        </g>
      </svg>
      <span class="contact-text">glen@glenhardesty-example.com</span>
    </div>

    <ul class="social-list">
      <li><span class="social-mark"></span>photoshare.example/glenshoots</li>
      <li><span class="social-mark"></span>friendbook.example/glenshoots</li>
      <li><span class="social-mark"></span>chirper.example/glenshoots</li>
    </ul>

    <div class="web-band">www.glenhardesty-example.com</div>
  </section>
</main>
</body>
</html>
```